Corvath Properties Business Card Design

We would now like to design business cards with the new Corvath Properties logo

Target Market(s)

Professional

Industry/Entity Type

Professional services

Contact Information for Business Card

Employee name, title, phone number, email address, corporate office address and logo.

Font styles to use
Sans Serif

Colors
0054AA
0677BA
7BADD7
CADEEF
E8F1F8

Requirements
Must have
• My logo
Should not have
• any other pictures or images besides my logo

```html
<!DOCTYPE html>
<html lang="en">
<head>
<meta charset="UTF-8">
<title>Corvath Properties Business Card</title>
<link href="https://fonts.googleapis.com/css2?family=Roboto+Condensed:wght@700&family=Arimo:wght@400;700&display=swap" rel="stylesheet">
<style>
  :root {
    --brand-blue: #1a7be0;
    --brand-deep: #0054aa;
    --brand-mid: #0677ba;
    --ink: #111418;
    --paper: #ffffff;
    --backdrop: #bfbfbf;
    --pattern-light: #2a88ea;
  }
  * { box-sizing: border-box; margin: 0; padding: 0; }
  html, body { width: 1200px; height: 800px; overflow: hidden; }
  body {
    background: var(--backdrop);
    display: flex;
    align-items: center;
    justify-content: center;
    gap: 40px;
    font-family: "Arimo", Arial, sans-serif;
  }
  .card {
    width: 540px;
    height: 310px;
    position: relative;
    box-shadow: 0 6px 18px rgba(0,0,0,0.18);
  }
  .card-front {
    background: var(--paper);
    border-bottom: 2px solid var(--brand-blue);
  }
  .brand-lockup {
    position: absolute;
    right: 36px;
    top: 44px;
    display: flex;
    align-items: center;
    gap: 12px;
  }
  .brand-square {
    width: 22px;
    height: 22px;
    background: var(--brand-blue);
  }
  .brand-name {
    font-family: "Roboto Condensed", Arial, sans-serif;
    font-weight: 700;
    font-size: 30px;
    line-height: 1;
    color: var(--brand-blue);
    text-transform: uppercase;
    letter-spacing: 0.5px;
  }
  .identity {
    position: absolute;
    left: 36px;
    top: 86px;
  }
  .person-name {
    font-family: "Roboto Condensed", Arial, sans-serif;
    font-weight: 700;
    font-size: 30px;
    color: var(--brand-blue);
    text-transform: uppercase;
    letter-spacing: -0.5px;
    line-height: 1;
  }
  .person-title {
    font-size: 15px;
    color: var(--ink);
    margin-top: 4px;
  }
  .divider {
    position: absolute;
    left: 36px;
    right: 36px;
    top: 164px;
    height: 1px;
    background: var(--brand-blue);
  }
  .contact-list {
    position: absolute;
    left: 36px;
    top: 180px;
    list-style: none;
  }
  .contact-item {
    display: flex;
    align-items: center;
    gap: 8px;
    font-size: 15px;
    color: var(--ink);
    line-height: 25px;
  }
  .contact-icon { width: 14px; height: 14px; flex: none; }
  .highlight { color: var(--brand-blue); }
  .address {
    position: absolute;
    right: 36px;
    top: 182px;
    font-size: 14px;
    color: var(--ink);
    line-height: 22px;
    font-style: normal;
  }
  .card-back {
    background: var(--brand-blue);
    overflow: hidden;
  }
  .pattern-field {
    position: absolute;
    inset: 0;
    background: linear-gradient(135deg, var(--pattern-light) 0%, var(--brand-blue) 55%, var(--brand-mid) 100%);
  }
  .back-mark {
    position: absolute;
    right: 40px;
    bottom: 60px;
    display: flex;
    align-items: center;
    gap: 8px;
  }
  .back-mark .brand-square { width: 14px; height: 14px; background: var(--paper); }
  .back-mark .brand-name { font-size: 18px; color: var(--paper); }
</style>
</head>
<body>
  <section class="card card-front" aria-label="Business card front">
    <div class="brand-lockup">
      <span class="brand-square"></span>
      <span class="brand-name">Corvath Properties</span>
    </div>
    <div class="identity">
      <h1 class="person-name">Elias Marlowe</h1>
      <p class="person-title">Managing Director</p>
    </div>
    <div class="divider"></div>
    <ul class="contact-list">
      <li class="contact-item">
        <svg class="contact-icon" viewBox="0 0 24 24"><path fill="#1a7be0" d="M6.6 10.8a15 15 0 0 0 6.6 6.6l2.2-2.2a1 1 0 0 1 1-.25 11.4 11.4 0 0 0 3.6.57 1 1 0 0 1 1 1V20a1 1 0 0 1-1 1A17 17 0 0 1 3 4a1 1 0 0 1 1-1h3.5a1 1 0 0 1 1 1c0 1.25.2 2.45.57 3.57a1 1 0 0 1-.25 1z"/></svg>
        044-987 654 321
      </li>
      <li class="contact-item">
        <svg class="contact-icon" viewBox="0 0 24 24"><rect x="2" y="5" width="20" height="14" fill="#1a7be0"/><path d="M2 5l10 8 10-8" fill="none" stroke="#fff" stroke-width="1.8"/></svg>
        hello@corvathmail.com
      </li>
      <li class="contact-item">
        <svg class="contact-icon" viewBox="0 0 24 24"><circle cx="12" cy="12" r="10" fill="#1a7be0"/><path d="M2 12h20M12 2c3 3 3 17 0 20M12 2c-3 3-3 17 0 20" fill="none" stroke="#fff" stroke-width="1.4"/></svg>
        www.<span class="highlight">corvathprops</span>.com
      </li>
    </ul>
    <address class="address">
      87, Harwell Street, Suite 4<br>
      60318, Northland
    </address>
  </section>

  <section class="card card-back" aria-label="Business card back">
    <div class="pattern-field" role="img" aria-label="Repeating tonal brand pattern across the card back"></div>
    <div class="back-mark">
      <span class="brand-square"></span>
      <span class="brand-name">Corvath Properties</span>
    </div>
  </section>
</body>
</html>
```